Harlow Reese, LLC Website

We are a small law firm in need of a website that contains the following:
1. Attractive main page
2. About us/attorney info for three people: Martin Harlow (attorney), Dean Reese (attorney), and Melissa Durant (legal assistant). We have bio's ready to submit.
3. Blog/video page. We'd like to post blogs and videos to help drive traffic
4. Multidistrict Litigation and Class Actions page, where we post information regarding active MDLs and Class actions that we are doing intake on.
Updates

Can you also please use the color "gold" in the design and logo? Thanks.

Industry/Entity Type

Legal

Coding

Coded - Design and coding required

Number of Pages Required

1 page

Colors
0054AA
0677BA
7BADD7
CADEEF
E8F1F8

Requirements
Must have
• 1. Attractive main page 2. About us/attorney info for three people: Martin Harlow (attorney), Dean Reese (attorney), and Melissa Durant (legal assistant). We have bio's ready to submit. 3. Blog/video page. We'd like to post blogs and videos to help drive traffic 4. Multidistrict Litigation and Class Actions page, where we post information regarding active MDLs and Class actions that we are doing intake on.

```html
<!DOCTYPE html>
<html lang="en">
<head>
<meta charset="UTF-8">
<title>Harlow Reese, LLC — Class Action &amp; MDL Lawyers</title>
<link href="https://fonts.googleapis.com/css2?family=Montserrat:wght@400;500;600;700;800&display=swap" rel="stylesheet">
<style>
:root{
  --blue:#1ea8f5;
  --blue-deep:#0054AA;
  --navy:#102a78;
  --ink:#1d1d1f;
  --text:#6b6b70;
  --line:#d9d9dc;
  --sky:#bde6fb;
  --dark:#1b1b1b;
  --white:#ffffff;
}
*{margin:0;padding:0;box-sizing:border-box}
html,body{width:1200px;height:4356px;overflow:hidden}
body{font-family:"Montserrat",sans-serif;color:var(--ink);background:var(--white);position:relative}
.abs{position:absolute}
.btn{position:absolute;display:flex;align-items:center;justify-content:center;font-size:12.5px;font-weight:700;text-transform:uppercase;letter-spacing:.2px;color:var(--white);background:var(--blue)}
.eyebrow{font-size:13px;font-weight:700;color:var(--navy);text-transform:uppercase}
.title{font-size:28px;font-weight:700;text-transform:uppercase;line-height:1.28;color:var(--ink)}
.copy{font-size:12.6px;line-height:22px;color:var(--text)}
.brand{display:flex;align-items:center;gap:10px;font-weight:700;color:var(--blue-deep);text-transform:uppercase;white-space:nowrap}
.brand .mark{background:var(--blue-deep);flex:none}

/* header */
.site-header{top:0;left:0;width:1200px;height:90px;background:var(--white)}
.site-header .brand{position:absolute;left:90px;top:27px;font-size:19px}
.site-header .brand .mark{width:36px;height:36px}
.nav{position:absolute;left:360px;top:38px;display:flex;gap:21px;font-size:11.3px;font-weight:500;color:#55555a;text-transform:uppercase}

/* hero */
.hero{top:90px;left:0;width:1200px;height:672px;background:linear-gradient(90deg,#1e1f22 0%,#3a3c40 38%,#8b8d91 70%,#62646a 100%)}
.hero h1{position:absolute;left:90px;top:160px;font-size:68px;font-weight:800;line-height:73px;color:var(--white);text-transform:uppercase}
.hero p{position:absolute;left:90px;top:386px;width:470px;font-size:12.6px;line-height:22px;color:var(--white)}
.hero .ghost{background:transparent;border:2px solid var(--white)}
.scroll-down{position:absolute;left:572px;top:592px;width:56px;height:56px;border-radius:50%;background:var(--white);display:flex;align-items:center;justify-content:center}

/* about */
.about-photo{left:144px;top:853px;width:371px;height:409px;background:linear-gradient(160deg,#c7d3dc 0%,#8a98a5 55%,#3b3f45 100%)}
.years{left:144px;top:1158px;width:131px;height:104px;background:var(--white);text-align:center;padding-top:12px}
.years b{display:block;font-size:38px;font-weight:500;line-height:40px}
.years span{display:block;font-size:13px;line-height:21px;text-transform:uppercase}

/* practice */
.card{position:absolute;top:1425px;width:246px;height:241px;border:1.5px solid var(--line);text-align:center;padding:0 14px}
.card .icon{width:66px;height:60px;margin:24px auto 0;border-radius:8px;background:linear-gradient(135deg,#d3eefd,#9bd6f9)}
.card h3{margin-top:12px;font-size:13.6px;font-weight:600;line-height:22px;text-transform:uppercase}
.card p{margin-top:8px;font-size:12.6px;line-height:22px;color:var(--text)}

/* blog */
.tabs{top:1927px;left:0;width:1200px;display:flex;justify-content:center;gap:60px;font-size:13.5px;font-weight:600;text-transform:uppercase}
.tabs .active{color:var(--navy);text-decoration:underline;text-underline-offset:4px}
.video{left:90px;top:1979px;width:1020px;height:450px;background:linear-gradient(180deg,#dcdedf 0%,#b9b6b0 45%,#6f7479 80%,#c7cbcd 100%)}
.play{position:absolute;left:459px;top:174px;width:102px;height:102px;border-radius:50%;background:var(--white);display:flex;align-items:center;justify-content:center;box-shadow:0 4px 14px rgba(0,0,0,.2)}

/* team */
.member{position:absolute;top:2626px;width:279px;height:303px;background:var(--sky)}
.member .tag{position:absolute;left:30px;top:264px;width:213px;height:78px;background:var(--white);box-shadow:0 6px 16px rgba(0,0,0,.1);text-align:center;padding-top:20px}
.member .tag b{display:block;font-size:13.6px;font-weight:700;text-transform:uppercase}
.member .tag span{display:block;font-size:12.4px;line-height:24px;color:#55555a;text-transform:uppercase}

/* mdl */
.checks{left:112px;top:3346px;list-style:none;font-size:12.6px;line-height:22.5px;color:var(--text)}
.checks li{display:flex;align-items:center;gap:8px}
.mdl-photo{left:625px;top:3067px;width:465px;height:448px;background:radial-gradient(ellipse at 60% 40%,#5a5d63 0%,#8f9297 40%,#e9eaeb 75%,#ffffff 100%)}

/* cta & footer */
.footer{left:0;top:3797px;width:1200px;height:559px;background:var(--dark)}
.cta{left:120px;top:3642px;width:960px;height:257px;background:var(--blue);text-align:center;color:var(--white)}
.cta h2{margin-top:57px;font-size:31px;font-weight:700;line-height:38px;text-transform:uppercase}
.cta p{margin:16px auto 0;width:640px;font-size:12.6px;line-height:22px}
.cta .btn{left:341px;top:177px;width:278px;height:42px;background:var(--white);color:var(--ink);font-weight:600}
.footer .brand{position:absolute;left:90px;top:281px;font-size:21px;color:var(--blue)}
.footer .brand .mark{width:44px;height:44px;background:var(--blue)}
.fcol h4{font-size:19px;font-weight:700;color:var(--white);text-transform:uppercase;margin-bottom:14px}
.fcol ul{list-style:none;font-size:14px;line-height:29px;color:#c9c9cc}
.contact-item{display:flex;gap:12px;margin-bottom:14px;font-size:13.5px;line-height:17px;color:var(--white)}
.contact-item small{display:block;font-size:12.4px;color:#c9c9cc}
.socials{display:flex;gap:6px}
.socials span{width:40px;height:40px;border-radius:50%;background:#55575b;border:2px solid #8c8e92}
.socials span:first-child{background:var(--blue);border-color:var(--blue)}
.rule{left:90px;top:4282px;width:1020px;height:1px;background:#4a4a4c}
.copyright{left:0;top:4306px;width:1200px;text-align:center;font-size:13.6px;color:var(--white)}
.to-top{left:1123px;top:4255px;width:52px;height:52px;border-radius:50%;background:var(--blue);display:flex;align-items:center;justify-content:center}
</style>
</head>
<body>

<header class="site-header abs">
  <div class="brand"><span class="mark"></span>Harlow Reese LLC</div>
  <nav class="nav"><span>Home</span><span>About</span><span>Legal Team</span><span>Blog &amp; Videos</span><span>MDLs &amp; Class Actions</span><span>Contact</span></nav>
  <a class="btn" style="left:935px;top:25px;width:175px;height:42px">Free Consultation</a>
</header>

<section class="hero abs" role="img" aria-label="Three attorneys in conversation in a bright office">
  <h1>Justice.<br>Dedication.<br>Results.</h1>
  <p>Experienced legal professionals fighting for your rights in class action and multidistrict litigation cases.</p>
  <a class="btn" style="left:90px;top:449px;width:152px;height:42px">Meet Our Team</a>
  <a class="btn ghost" style="left:254px;top:449px;width:164px;height:42px">See Active Cases</a>
  <div class="scroll-down"><svg width="20" height="20" viewBox="0 0 20 20"><path d="M10 3v13M4 10l6 6 6-6" fill="none" stroke="#333" stroke-width="1.6"/></svg></div>
</section>

<div class="about-photo abs" role="img" aria-label="Bronze statue of Lady Justice with scales beside law books"></div>
<div class="years abs"><b>29+</b><span>Year of<br>Experience</span></div>
<div class="eyebrow abs" style="left:568px;top:895px">Who We Are</div>
<h2 class="title abs" style="left:568px;top:917px">Your Trusted Legal Team<br>for Complex Cases</h2>
<p class="copy abs" style="left:568px;top:1000px;width:500px">At Harlow Reese Law Group, we specialize in representing individuals and families impacted by corporate negligence, unsafe products, and deceptive practices. We combine personal attention with national-level legal experience, and we’re here to make sure your voice is heard.</p>
<p class="copy abs" style="left:568px;top:1107px;width:500px">Whether you’re exploring a class action lawsuit or looking for support in a multidistrict litigation case, our team brings commitment and clarity to every client we serve.</p>
<a class="btn" style="left:568px;top:1193px;width:140px;height:44px">Learn More</a>

<h2 class="title abs" style="left:0;top:1360px;width:1200px;text-align:center">Practice Areas</h2>
<div class="card" style="left:90px"><div class="icon" role="img" aria-label="Courthouse with gavel icon"></div><h3>Multidistrict Litigation (MDLs)</h3><p>Legal representation in nation wide product &amp; pharmaceutical litigation.</p></div>
<div class="card" style="left:350px"><div class="icon" role="img" aria-label="Gavel icon"></div><h3>Class Action Lawsuits</h3><p>Fighting for groups of individuals harmed by corporations and institutions.</p></div>
<div class="card" style="left:608px"><div class="icon" role="img" aria-label="Protecting hand over a family icon"></div><h3>Consumer Protection</h3><p>Standing up for consumers deceived or wronged by businesses.</p></div>
<div class="card" style="left:865px"><div class="icon" role="img" aria-label="Injured person icon"></div><h3>Mass Torts &amp; Injury Claims</h3><p>Helping those who’ve been physically or financially injured by negligence.</p></div>
<a class="btn" style="left:483px;top:1703px;width:234px;height:43px">Explore Practice Areas +</a>

<div class="eyebrow abs" style="left:0;top:1855px;width:1200px;text-align:center">Blog &amp; Video Center</div>
<h2 class="title abs" style="left:0;top:1876px;width:1200px;text-align:center">Insights, Updates &amp; Legal Resources</h2>
<div class="tabs abs"><span>Legal Explainers</span><span class="active">Video Briefings</span><span>Case Updates</span><span>Community News</span></div>
<div class="video abs" role="img" aria-label="Video thumbnail of four legal professionals seated at a conference table">
  <div class="play"><svg width="34" height="38" viewBox="0 0 34 38"><path d="M4 2l28 17L4 36z" fill="#0c1c5c"/></svg></div>
</div>

<div class="eyebrow abs" style="left:0;top:2541px;width:1200px;text-align:center">Our Legal Team</div>
<h2 class="title abs" style="left:0;top:2563px;width:1200px;text-align:center">Meet the Team Behind the Mission</h2>
<div class="member" style="left:169px" role="img" aria-label="Portrait of Martin Harlow"><div class="tag"><b>Martin Harlow</b><span>Attorney at Law</span></div></div>
<div class="member" style="left:460px" role="img" aria-label="Portrait of Dean Reese"><div class="tag"><b>Dean Reese</b><span>Attorney at Law</span></div></div>
<div class="member" style="left:752px" role="img" aria-label="Portrait of Melissa Durant"><div class="tag"><b>Melissa Durant</b><span>Legal Assistant</span></div></div>

<div class="eyebrow abs" style="left:113px;top:3153px">MDLs &amp; Class Actions</div>
<h2 class="title abs" style="left:113px;top:3174px">Ongoing MDLs &amp; Class Action<br>Investigations</h2>
<p class="copy abs" style="left:112px;top:3257px;width:510px">We’re currently investigating and accepting claims for several high-impact legal matters. If you think you may qualify, reach out today for a free consultation.</p>
<ul class="checks abs">
  <li><svg width="13" height="13" viewBox="0 0 13 13"><circle cx="6.5" cy="6.5" r="6.5" fill="var(--blue)"/><path d="M3.5 6.7l2 2 4-4" fill="none" stroke="#fff" stroke-width="1.5"/></svg>Drug &amp; Medical Device MDLs.</li>
  <li><svg width="13" height="13" viewBox="0 0 13 13"><circle cx="6.5" cy="6.5" r="6.5" fill="var(--blue)"/><path d="M3.5 6.7l2 2 4-4" fill="none" stroke="#fff" stroke-width="1.5"/></svg>Defective Consumer Products.</li>
  <li><svg width="13" height="13" viewBox="0 0 13 13"><circle cx="6.5" cy="6.5" r="6.5" fill="var(--blue)"/><path d="M3.5 6.7l2 2 4-4" fill="none" stroke="#fff" stroke-width="1.5"/></svg>Toxic Exposure Cases.</li>
  <li><svg width="13" height="13" viewBox="0 0 13 13"><circle cx="6.5" cy="6.5" r="6.5" fill="var(--blue)"/><path d="M3.5 6.7l2 2 4-4" fill="none" stroke="#fff" stroke-width="1.5"/></svg>Data Breach Class Actions.</li>
</ul>
<a class="btn" style="left:112px;top:3449px;width:234px;height:42px">See Active Investigations +</a>
<div class="mdl-photo abs" role="img" aria-label="Attorney seated in an armchair reviewing a tablet"></div>

<footer class="footer abs">
  <div class="brand"><span class="mark"></span>Harlow Reese LLC</div>
  <div class="fcol abs" style="left:441px;top:196px"><h4>Quick Link</h4>
    <ul><li>Home</li><li>About</li><li>Legal Team</li><li>Blog &amp; Videos</li><li>MDLs &amp; Class Actions</li><li>Contact</li></ul></div>
  <div class="fcol abs" style="left:666px;top:196px"><h4>Contact Us</h4>
    <div class="contact-item"><svg width="14" height="14" viewBox="0 0 24 24"><path d="M6.6 10.8a15 15 0 006.6 6.6l2.2-2.2a1 1 0 011-.25 11.4 11.4 0 003.6.57 1 1 0 011 1V20a1 1 0 01-1 1A17 17 0 013 4a1 1 0 011-1h3.5a1 1 0 011 1c0 1.25.2 2.45.57 3.57a1 1 0 01-.25 1z" fill="var(--blue)"/></svg><div>Phone<small>( 0123 ) 555-0148</small></div></div>
    <div class="contact-item"><svg width="14" height="14" viewBox="0 0 24 24"><path d="M2 5h20v14H2z" fill="var(--blue)"/><path d="M2 5l10 8 10-8" fill="none" stroke="#1b1b1b" stroke-width="1.6"/></svg><div>Email<small>hello@harlowreese.example</small></div></div>
    <div class="contact-item"><svg width="14" height="16" viewBox="0 0 24 28"><path d="M12 0a9 9 0 00-9 9c0 7 9 19 9 19s9-12 9-19a9 9 0 00-9-9z" fill="var(--blue)"/><circle cx="12" cy="9" r="3.5" fill="#1b1b1b"/></svg><div>Location<small>12 Linden Court, Suite 4,<br>Fairview 55946 United States</small></div></div>
  </div>
  <div class="fcol abs" style="left:931px;top:196px"><h4>Follow Us</h4>
    <div class="socials"><span></span><span></span><span></span><span></span></div></div>
</footer>

<section class="cta abs">
  <h2>Let’s Discuss Your Case – No Cost,<br>No Obligation</h2>
  <p>Our legal consultations are free, confidential, and designed to give you clear direction. Take the first step today.</p>
  <a class="btn">Schedule a Free Consultation</a>
</section>

<div class="rule abs"></div>
<div class="copyright abs">2025 HARLOW REESE LLC LAWYER Resources, All right Reserved</div>
<div class="to-top abs"><svg width="16" height="16" viewBox="0 0 16 16"><path d="M3 10l5-5 5 5" fill="none" stroke="#fff" stroke-width="1.8"/></svg></div>

</body>
</html>
```